Gradvolt

I have a web site GRADVOLT.com that is in serious need of a re-design. The site is mean't to be a portal for an app that I have called GRADVOLT which you can see in the App Market or googleplay. Take a look and see what you can do.
Updates

Project Deadline Extended
Reason: Still working with designers. The "look" is not quite there but a lot of progress has been made. RM

Industry/Entity Type

Store

```html
<!DOCTYPE html>
<html lang="en">
<head>
<meta charset="utf-8">
<title>Gradvolt – Sports Portal</title>
<link rel="stylesheet" href="https://fonts.googleapis.com/css2?family=Roboto+Condensed:wght@400;700&family=Open+Sans:ital,wght@0,400;0,600;1,600;1,700&display=swap">
<style>
:root{
  --navy:#17367a;
  --blue:#1d3f8e;
  --nav-active:#4a78b8;
  --green:#2c8a2c;
  --panel-head:#d6d6d6;
  --panel-body:#ffffff;
  --row:#ececec;
  --row-alt:#f6f6f6;
  --text:#333333;
  --muted:#666666;
  --dark:#1b1b1b;
}
*{box-sizing:border-box;margin:0;padding:0}
html,body{width:843px;height:1200px;overflow:hidden}
body{font-family:"Open Sans",Arial,sans-serif;color:var(--text);font-size:10px}
.stage{position:relative;width:843px;height:1200px;overflow:hidden}
.backdrop{position:absolute;inset:0;background:radial-gradient(ellipse at 50% 45%,#9a9a9a 0%,#7d7d7d 55%,#6a6a6a 100%)}
.abs{position:absolute}
.brand{left:46px;top:34px;font-family:"Roboto Condensed",sans-serif;font-weight:700;font-size:40px;color:var(--navy);display:flex;align-items:center;gap:10px;letter-spacing:.5px}
.brand-mark{width:26px;height:26px;border-radius:50%;background:var(--green)}
.social{left:570px;top:23px;display:flex;gap:9px}
.social span{width:24px;height:24px;background:#dcdcdc;border:1px solid #c4c4c4}
.social span:first-child{background:#3b5ea8;border-color:#3b5ea8}
.search{left:570px;top:66px;width:226px;height:32px;border:2px solid var(--green);background:#f2f2f2;display:flex}
.search .field{flex:1;font-style:italic;color:#888;font-size:10px;padding:9px 7px}
.search .go{width:32px;background:var(--green);display:flex;align-items:center;justify-content:center}
.nav{left:0;top:99px;width:843px;height:38px;background:linear-gradient(#e6e6e6,#cfcfcf);border-top:1px solid #f4f4f4;border-bottom:1px solid #aaa}
.nav a{position:absolute;top:0;height:38px;line-height:38px;font-family:"Roboto Condensed",sans-serif;font-size:13.5px;color:#2a2a2a;text-decoration:none;text-transform:uppercase}
.nav a.active{background:var(--nav-active);color:#fff;width:76px;text-align:center}
.photo{background:linear-gradient(135deg,#6b4a2a,#c28a55 40%,#3c3c5a 75%,#222)}
.photo.pitch{background:linear-gradient(160deg,#5a8a4a,#9cc08a 50%,#e8e8e8)}
.photo.field{background:linear-gradient(160deg,#b98b5c,#d9b48b 55%,#7a5a3c)}
.photo.player{background:linear-gradient(150deg,#3a2a20,#a33a3a 45%,#2a3a8a 70%,#222)}
.photo.court{background:linear-gradient(140deg,#2a2a2a,#8a5a3a 50%,#b07a55)}
.hero{left:46px;top:156px;width:506px;height:248px}
.hero-caption{position:absolute;left:0;right:0;bottom:0;height:51px;background:rgba(0,0,0,.6);color:#fff;padding:6px 11px}
.hero-caption h2{font-weight:400;font-size:15.5px;font-family:"Open Sans",sans-serif}
.hero-caption p{font-size:9px;font-weight:600;margin-top:3px}
.panel{position:absolute;background:var(--panel-body);box-shadow:0 1px 3px rgba(0,0,0,.3)}
.panel-head{height:33px;background:linear-gradient(#e4e4e4,#cbcbcb);display:flex;align-items:center;justify-content:space-between;padding:0 14px 0 15px}
.panel-head h3{font-family:"Roboto Condensed",sans-serif;font-weight:400;font-size:15px;color:var(--navy);text-transform:uppercase}
.dots{display:flex;gap:3px}
.dots i{width:4px;height:4px;border-radius:50%;background:#444}
.dots i:first-child{background:var(--navy)}
.result{left:570px;top:156px;width:226px;height:198px}
.pitch-board{height:165px;background:linear-gradient(#1d3a1d,#2f6a2f 55%,#3c7a3c);color:#fff;text-align:center;position:relative}
.pitch-board .league{padding-top:28px;font-family:"Roboto Condensed",sans-serif;font-size:15px}
.crest{position:absolute;top:75px;width:40px;height:50px;border-radius:4px 4px 20px 20px}
.crest.home{left:24px;background:#c8202a}
.crest.away{right:24px;background:#e8e8e8}
.score{position:absolute;left:0;right:0;top:72px;font-family:"Roboto Condensed",sans-serif;font-size:34px;font-weight:700}
.date{position:absolute;left:0;right:0;top:115px;font-size:9px;font-weight:600}
.team{position:absolute;top:141px;font-size:10px;font-weight:600}
.tabs{left:570px;top:372px;width:226px;height:239px}
.tab-row{display:flex;height:32px}
.tab-row div{flex:1;display:flex;align-items:center;justify-content:center;font-family:"Roboto Condensed",sans-serif;font-size:15px;text-transform:uppercase}
.tab-row .off{background:linear-gradient(#e4e4e4,#cbcbcb);color:var(--navy)}
.tab-row .on{background:var(--navy);color:#fff}
.item{display:flex;gap:7px;padding:7px 7px;height:69px;border-bottom:2px solid #fff;background:var(--row-alt)}
.item:first-of-type{background:#dcdcdc}
.item .thumb{width:55px;height:51px;flex:none}
.item h4{font-style:italic;font-weight:600;font-size:11px;color:#111;margin-top:1px}
.item h4.hl{color:var(--blue)}
.item p{font-size:9.5px;color:#555;line-height:14px;margin-top:3px}
.news{width:506px;left:46px}
.card{position:absolute;width:149px}
.card .pic{height:90px;position:relative}
.tag{position:absolute;left:0;bottom:0;background:rgba(20,20,20,.85);color:#fff;font-style:italic;font-weight:600;font-size:11px;padding:3px 8px}
.tag.lead{background:var(--navy)}
.play{position:absolute;right:0;bottom:0;width:28px;height:21px;background:rgba(20,20,20,.85);display:flex;align-items:center;justify-content:center}
.card h4{font-size:12px;font-weight:600;color:#222;margin-top:9px}
.card h4.hl{color:var(--blue)}
.meta{font-size:9.5px;color:#555;margin-top:5px;display:flex;gap:12px;align-items:center}
.meta span{display:flex;gap:4px;align-items:center}
.players{left:46px;top:630px;width:243px;height:203px}
.players .pic{height:170px;position:relative}
.players .cap{position:absolute;left:0;right:0;bottom:0;height:27px;background:rgba(0,0,0,.55);color:#fff;display:flex;align-items:center;gap:20px;padding-left:10px;font-size:10.5px}
.players .cap b{font-style:italic;font-weight:600}
.players .cap span{color:#bbb;font-size:9.5px}
.schedule{left:308px;top:630px;width:244px;height:203px}
.sched-row{height:56px;display:flex;gap:8px;padding:7px 8px;border-bottom:2px solid #fff;background:var(--row-alt)}
.sched-row.alt{background:#dedede;justify-content:space-between}
.sched-row .thumb{width:44px;height:38px;flex:none}
.sched-row h4{font-style:italic;font-weight:600;font-size:11.5px;color:var(--blue)}
.sched-row .place{font-size:9.5px;color:#444;margin-top:2px}
.sched-row .meta{margin-top:2px}
.performance{left:570px;top:630px;width:226px;height:308px}
.performance .item{height:69px}
.sponsors{left:570px;top:957px;width:226px;height:81px}
.sponsor-row{display:flex;justify-content:space-between;padding:8px 10px}
.sponsor-row span{width:36px;height:36px;border-radius:50%}
.footer{left:0;top:1057px;width:843px;height:104px;background:rgba(200,200,200,.85)}
.footer h3{position:absolute;font-family:"Roboto Condensed",sans-serif;font-weight:700;font-size:14.5px;color:var(--navy);text-transform:uppercase;top:13px}
.store{position:absolute;top:41px;width:157px;height:46px;background:linear-gradient(#3a3a3a,#0e0e0e);border:1px solid #777;border-radius:6px;display:flex;align-items:center;gap:10px;padding-left:14px;color:#fff}
.store .sq{width:20px;height:20px;background:#fff;border-radius:3px;flex:none}
.store small{display:block;font-size:9.5px;font-weight:600}
.store strong{display:block;font-size:17px;font-weight:600;line-height:19px}
.subscribe{position:absolute;left:510px;top:43px;width:286px;height:31px;background:var(--dark);display:flex}
.subscribe .env{width:44px;display:flex;align-items:center;justify-content:center}
.subscribe .field{flex:1;color:#eee;font-style:italic;font-weight:600;font-size:10px;padding:9px 4px}
.subscribe .go{width:32px;background:var(--navy);display:flex;align-items:center;justify-content:center}
.bottom{left:0;top:1161px;width:843px;height:39px;background:#cfcfcf;font-size:10px;color:#333}
.crumbs{position:absolute;left:46px;top:13px}
.crumbs a{color:#333;text-decoration:none}
.crumbs a:first-child{color:var(--blue)}
.copy{position:absolute;right:47px;top:13px}
</style>
</head>
<body>
<div class="stage">
  <div class="backdrop" role="img" aria-label="Grey-toned stadium and football pitch background"></div>

  <div class="abs brand"><span class="brand-mark"></span>Gradvolt</div>

  <div class="abs social" aria-label="Social links"><span></span><span></span><span></span><span></span><span></span><span></span><span></span></div>

  <div class="abs search">
    <div class="field">Search</div>
    <div class="go"><svg width="16" height="16" viewBox="0 0 16 16"><circle cx="9.5" cy="6.5" r="4.5" fill="none" stroke="#fff" stroke-width="2"/><line x1="6.3" y1="9.7" x2="2" y2="14" stroke="#fff" stroke-width="2.5"/></svg></div>
  </div>

  <nav class="abs nav">
    <a class="active" href="#" style="left:46px">Home</a>
    <a href="#" style="left:137px">About Us</a>
    <a href="#" style="left:231px">Events</a>
    <a href="#" style="left:310px">Live Scores</a>
    <a href="#" style="left:421px">Sports News</a>
    <a href="#" style="left:535px">Photos</a>
    <a href="#" style="left:620px">FAQs</a>
    <a href="#" style="left:687px">Contact Us</a>
  </nav>

  <section class="abs hero photo court" role="img" aria-label="Basketball players reaching for the ball in an arena">
    <div class="hero-caption">
      <h2>Lorem ipsum dolor sit amet consectetur adipiscing elit</h2>
      <p>Proin ornare augue purus, eu cursus nibh vestibulum quis. Sed id nisi eget odio consectetur imperdiet.</p>
    </div>
  </section>

  <section class="panel result">
    <div class="panel-head"><h3>Recent Results</h3><div class="dots"><i></i><i></i><i></i><i></i><i></i><i></i><i></i></div></div>
    <div class="pitch-board">
      <div class="league">Prima League</div>
      <div class="crest home"></div>
      <div class="crest away"></div>
      <div class="score">2 - 2</div>
      <div class="date">02 Jan 2013</div>
      <div class="team" style="left:30px">Rovena</div>
      <div class="team" style="right:30px">Calder</div>
    </div>
  </section>

  <section class="panel tabs">
    <div class="tab-row"><div class="off">Popular</div><div class="on">Latest</div></div>
    <div class="item"><div class="thumb photo court" role="img" aria-label="Basketball player portrait"></div><div><h4 class="hl">Lorem ipsum dolor sit .</h4><p>Proin ornare augue purus, eu cursus nibh vestibulum quis.</p></div></div>
    <div class="item"><div class="thumb photo court" role="img" aria-label="Basketball player portrait"></div><div><h4>Lorem ipsum dolor sit .</h4><p>Proin ornare augue purus, eu cursus nibh vestibulum quis.</p></div></div>
    <div class="item"><div class="thumb photo court" role="img" aria-label="Basketball player portrait"></div><div><h4>Lorem ipsum dolor sit .</h4><p>Proin ornare augue purus, eu cursus nibh vestibulum quis.</p></div></div>
  </section>

  <section class="panel news" style="top:423px;height:188px">
    <div class="panel-head"><h3>Latest News</h3><div class="dots"><i></i><i></i><i></i><i></i><i></i><i></i><i></i></div></div>
    <article class="card" style="left:15px;top:48px"><div class="pic photo court" role="img" aria-label="Basketball game action"><span class="tag lead">Basketball</span></div><h4 class="hl">Lorem ipsum dolor sit .</h4><div class="meta"><span>⏰ 1:40 pm</span><span>▦ 25 Nov 2013</span></div></article>
    <article class="card" style="left:178px;top:48px"><div class="pic photo pitch" role="img" aria-label="Football players at the goal"><span class="tag">Football</span></div><h4>Lorem ipsum dolor sit .</h4><div class="meta"><span>⏰ 1:40 pm</span><span>▦ 25 Nov 2013</span></div></article>
    <article class="card" style="left:341px;top:48px"><div class="pic photo field" role="img" aria-label="Baseball player sliding into base"><span class="tag">Baseball</span></div><h4>Lorem ipsum dolor sit .</h4><div class="meta"><span>⏰ 1:40 pm</span><span>▦ 25 Nov 2013</span></div></article>
  </section>

  <section class="panel players">
    <div class="panel-head"><h3>Players</h3><div class="dots"><i></i><i></i><i></i><i></i><i></i><i></i><i></i></div></div>
    <div class="pic photo player" role="img" aria-label="Footballer in a striped kit raising his hand">
      <div class="cap"><b>Theo Marlo Football</b><span>Valdoria</span></div>
    </div>
  </section>

  <section class="panel schedule">
    <div class="panel-head"><h3>Schedules</h3></div>
    <div class="sched-row"><div class="thumb photo court" role="img" aria-label="Basketball player portrait"></div><div><h4>Rovena</h4><div class="meta"><span>⏰ 1:40 pm</span><span>▦ 25 Nov 2013</span></div><div class="place">Lorem ispum place name</div></div></div>
    <div class="sched-row alt"><div><h4>Rovena</h4><div class="meta"><span>⏰ 1:40 pm</span><span>▦ 25 Nov 2013</span></div><div class="place">Lorem ispum plase name</div></div><div class="thumb photo player" role="img" aria-label="Footballer portrait"></div></div>
    <div class="sched-row"><div class="thumb photo field" role="img" aria-label="Baseball play at base"></div><div><h4>Rovena</h4><div class="meta"><span>⏰ 1:40 pm</span><span>▦ 25 Nov 2013</span></div><div class="place">Lorem ispum plase name</div></div></div>
  </section>

  <section class="panel performance">
    <div class="panel-head"><h3>Past Team Performance</h3></div>
    <div class="item"><div class="thumb photo court" role="img" aria-label="Basketball player portrait"></div><div><h4 class="hl">Rovena</h4><p>Lorem ispum plase ispum<br>Proin ornare augue lorempu</p></div></div>
    <div class="item"><div class="thumb photo court" role="img" aria-label="Basketball player portrait"></div><div><h4>Lorem ipsum dolor sit .</h4><p>Proin ornare augue purus, eu cursus nibh vestibulum quis.</p></div></div>
    <div class="item"><div class="thumb photo player" role="img" aria-label="Footballer portrait"></div><div><h4>Lorem ipsum dolor sit .</h4><p>Proin ornare augue purus, eu cursus nibh vestibulum quis.</p></div></div>
    <div class="item"><div class="thumb photo field" role="img" aria-label="Baseball play at base"></div><div><h4>Lorem ipsum dolor sit .</h4><p>Proin ornare augue purus, eu cursus nibh vestibulum quis.</p></div></div>
  </section>

  <section class="panel news" style="top:851px;height:187px">
    <div class="panel-head"><h3>Latest News</h3><div class="dots"><i></i><i></i><i></i><i></i><i></i><i></i><i></i></div></div>
    <article class="card" style="left:15px;top:48px"><div class="pic photo court" role="img" aria-label="Basketball game video still"><span class="tag lead">Basketball</span><span class="play"><svg width="16" height="16" viewBox="0 0 16 16"><circle cx="8" cy="8" r="7" fill="none" stroke="#fff" stroke-width="1.5"/><path d="M6.5 5v6l4.5-3z" fill="#fff"/></svg></span></div><h4 class="hl">Lorem ipsum dolor sit .</h4><div class="meta"><span>⏰ 1:40 pm</span><span>▦ 25 Nov 2013</span></div></article>
    <article class="card" style="left:178px;top:48px"><div class="pic photo pitch" role="img" aria-label="Football match video still"><span class="tag">Football</span><span class="play"><svg width="16" height="16" viewBox="0 0 16 16"><circle cx="8" cy="8" r="7" fill="none" stroke="#fff" stroke-width="1.5"/><path d="M6.5 5v6l4.5-3z" fill="#fff"/></svg></span></div><h4>Lorem ipsum dolor sit .</h4><div class="meta"><span>⏰ 1:40 pm</span><span>▦ 25 Nov 2013</span></div></article>
    <article class="card" style="left:341px;top:48px"><div class="pic photo field" role="img" aria-label="Baseball game video still"><span class="tag">Baseball</span><span class="play"><svg width="16" height="16" viewBox="0 0 16 16"><circle cx="8" cy="8" r="7" fill="none" stroke="#fff" stroke-width="1.5"/><path d="M6.5 5v6l4.5-3z" fill="#fff"/></svg></span></div><h4>Lorem ipsum dolor sit .</h4><div class="meta"><span>⏰ 1:40 pm</span><span>▦ 25 Nov 2013</span></div></article>
  </section>

  <section class="panel sponsors">
    <div class="panel-head"><h3>Our Sponsors</h3><div class="dots"><i></i><i></i><i></i><i></i><i></i><i></i><i></i></div></div>
    <div class="sponsor-row"><span style="background:#1f3a7a"></span><span style="background:#d9c27a"></span><span style="background:#3a7ac8"></span><span style="background:#c8303a"></span><span style="background:#d84a2a"></span></div>
  </section>

  <footer class="abs footer">
    <h3 style="left:46px">Gradvolt Mobile Apps Are Here</h3>
    <a class="store" style="left:46px"><span class="sq"></span><span><small>Available on the</small><strong>App Market</strong></span></a>
    <a class="store" style="left:216px"><span class="sq"></span><span><small>Get it on</small><strong>Play Market</strong></span></a>
    <h3 style="left:510px">Subscribe With Us:</h3>
    <div class="subscribe">
      <div class="env"><svg width="30" height="20" viewBox="0 0 30 20"><rect x="1" y="1" width="28" height="18" fill="none" stroke="#555" stroke-width="1.5"/><path d="M1 1l14 10 14-10" fill="none" stroke="#555" stroke-width="1.5"/></svg></div>
      <div class="field">Enter your Email...</div>
      <div class="go"><svg width="16" height="16" viewBox="0 0 16 16"><path d="M1 2l14 6-14 6 3-6z" fill="#fff"/></svg></div>
    </div>
  </footer>

  <div class="abs bottom">
    <div class="crumbs"><a href="#">Home</a> / <a href="#">About Us</a> / <a href="#">Events</a> / <a href="#">Live Scores</a> / <a href="#">News</a> / <a href="#">Sports</a> / <a href="#">Photos</a> / <a href="#">Faqs</a> / <a href="#">Contact Us</a></div>
    <div class="copy">© 2014 Gradvolt. All right reserved</div>
  </div>
</div>
</body>
</html>
```